Professional Business Card for Commercial Cleaning Company

We need a business card that represents our commercial janitorial cleaning company and represent several brands for our company so we do not want to highlight the logo too much. We want something that says we are professional.
Notes:No website or address as we have many locations and many websites and companies under our corporate name of "Brightvale Holdings, LLC" . Every time we hand a customer a business card they have contacted us via another brand we own but we don't want to have 21 business cards so we want to not focus on Brightvale Holdings, LLC too much since people will automatically ask "What is Brightvale Holdings, LLC" Example: Noodle Barn and Wrap Lantern restaurants are owned by "Zest! Brands" is the corporation name. Same principle here. Except we do not advertise at this time that all of our brands are connected. Hope this helps.
Target Market(s)
Commercial Cleaning
Industry/Entity Type
Janitorial Service
Contact Information for Business Card
Milo Jarvis
Business Development
555-382-9047
sales@brightvaleholdingsllc.example
Requirements
Must have
- Logo with contact information, need to be able to easily edit contact info for others in my office.
Nice to have
- Professional Image. Like to see a colorful bold look and a more standard business card look.
Should not have
- Any type of cleaning icons, tools, people or water.

```html
<!DOCTYPE html>
<html lang="en">
<head>
<meta charset="utf-8">
<title>Brightvale Holdings, LLC – Business Card</title>
<link rel="stylesheet" href="https://fonts.googleapis.com/css2?family=Montserrat:wght@700&family=Questrial&display=swap">
<style>
  :root {
    --page-bg: #e9eaec;
    --navy: #1f3f7a;
    --name-navy: #1d3a78;
    --green: #5aa532;
    --ink: #454545;
    --white: #ffffff;
  }
  * { box-sizing: border-box; margin: 0; padding: 0; }
  html, body {
    width: 1200px;
    height: 780px;
    overflow: hidden;
    background: var(--page-bg);
  }
  .canvas {
    position: relative;
    width: 1200px;
    height: 780px;
    display: flex;
    flex-direction: column;
    align-items: center;
    justify-content: center;
    gap: 40px;
  }
  .card {
    width: 560px;
    height: 320px;
    box-shadow: 0 6px 18px rgba(0, 0, 0, 0.18);
  }
  .card-front {
    background: var(--navy);
    display: flex;
    align-items: center;
    justify-content: center;
  }
  .brand-name {
    font-family: "Questrial", sans-serif;
    font-size: 34px;
    color: var(--white);
    letter-spacing: 0.5px;
  }
  .card-back {
    background: var(--white);
    display: flex;
    align-items: center;
    justify-content: center;
    gap: 22px;
    padding-bottom: 20px;
  }
  .person {
    text-align: right;
  }
  .person-name {
    font-family: "Montserrat", sans-serif;
    font-weight: 700;
    font-size: 24px;
    color: var(--name-navy);
    line-height: 1.1;
  }
  .person-title {
    font-family: "Questrial", sans-serif;
    font-size: 15px;
    color: var(--ink);
    margin-top: 3px;
  }
  .divider {
    width: 2px;
    height: 50px;
    background: var(--green);
  }
  .contact-list {
    list-style: none;
    font-family: "Questrial", sans-serif;
    font-size: 15px;
    color: var(--ink);
    display: flex;
    flex-direction: column;
    gap: 5px;
  }
  .contact-item {
    display: flex;
    align-items: center;
    gap: 9px;
  }
  .contact-icon {
    width: 11px;
    height: 11px;
    flex: none;
  }
</style>
</head>
<body>
  <main class="canvas">
    <section class="card card-front" aria-label="Card front">
      <p class="brand-name">Brightvale Holdings, LLC</p>
    </section>

    <section class="card card-back" aria-label="Card back">
      <div class="person">
        <h1 class="person-name">Milo Jarvis</h1>
        <p class="person-title">Business Development</p>
      </div>
      <span class="divider" aria-hidden="true"></span>
      <ul class="contact-list">
        <li class="contact-item">
          <svg class="contact-icon" viewBox="0 0 24 24" aria-hidden="true">
            <path fill="#5aa532" d="M6.6 10.8a15.2 15.2 0 0 0 6.6 6.6l2.2-2.2c.3-.3.7-.4 1-.2 1.1.4 2.3.6 3.6.6.6 0 1 .4 1 1V20c0 .6-.4 1-1 1A17 17 0 0 1 3 4c0-.6.4-1 1-1h3.5c.6 0 1 .4 1 1 0 1.3.2 2.5.6 3.6.1.3 0 .7-.2 1z"/>
          </svg>
          <span>555-382-9047</span>
        </li>
        <li class="contact-item">
          <svg class="contact-icon" viewBox="0 0 24 24" aria-hidden="true">
            <rect x="2.5" y="5" width="19" height="14" rx="1.5" fill="none" stroke="#5aa532" stroke-width="2.4"/>
            <path d="M3 6l9 7 9-7" fill="none" stroke="#5aa532" stroke-width="2.4"/>
          </svg>
          <span>sales@brightvaleholdingsllc.example</span>
        </li>
      </ul>
    </section>
  </main>
</body>
</html>
```